BLUE FORGE (Business Card for Training Company)

Blue Forge is a training and consultancy company with a focus on executive protection and medical. I would like the card to be nice and sharp, not overdone and in black and red. I would also like it to highlight that it is "A Tavmont Company"

I would like it to be simple and highlight a few things.

1. Name
2. Title
3. Phone Number
4. Email

I would also like www.tavmontgroup.example/blue-forge to be on the card somewhere.

Target Market(s)

Security Companies

Industry/Entity Type

Security

Contact Information for Business Card

Blue Forge is a training and consultancy company with a focus on executive protection and medical. I would like the card to be nice and sharp, not overdone and in black and red. I would also like it to highlight that it is "A Tavmont Company" I would like it to be simple and highlight a few things. 1. Name 2. Title 3. Phone Number 4. Email I would also like www.tavmontgroup.example/blue-forge to be on the card somewhere.

Requirements
Must have
• A Tavmont Company listed on the card and the website
Nice to have
• Highlight Medical Training, Consultancy & Executive Protection Courses

```html
<!DOCTYPE html>
<html lang="en">
<head>
<meta charset="utf-8">
<title>Blue Forge Business Card</title>
<link href="https://fonts.googleapis.com/css2?family=Roboto+Condensed:wght@700&family=Arimo:wght@400;700&display=swap" rel="stylesheet">
<style>
  :root {
    --wine: #6a0e13;
    --ink: #1f1f1f;
    --paper: #ffffff;
    --stage: #e6e4e2;
    --muted: #3a3a3a;
  }
  * { margin: 0; padding: 0; box-sizing: border-box; }
  html, body { width: 1200px; height: 960px; overflow: hidden; }
  body {
    background: var(--stage);
    position: relative;
    font-family: "Arimo", Arial, sans-serif;
  }
  .card {
    position: absolute;
    width: 560px;
    height: 320px;
    overflow: hidden;
    box-shadow: 0 6px 18px rgba(0,0,0,0.18);
  }
  /* Front side */
  .card--front {
    left: 150px; top: 110px;
    background: var(--wine);
    color: var(--paper);
    font-family: "Roboto Condensed", "Arial Narrow", sans-serif;
    font-weight: 700;
    text-align: center;
  }
  .front__brand {
    position: absolute;
    top: 58px; left: 0; right: 0;
    font-size: 64px;
    line-height: 0.92;
    letter-spacing: 2px;
  }
  .front__cta {
    position: absolute;
    top: 222px; left: 0; right: 0;
    font-size: 17px;
    letter-spacing: 1px;
  }
  .front__url {
    position: absolute;
    top: 250px; left: 0; right: 0;
    font-size: 24px;
    letter-spacing: 0.5px;
  }
  /* Back side */
  .card--back {
    left: 490px; top: 530px;
    background: var(--paper);
  }
  .back__swoosh { position: absolute; inset: 0; }
  .back__tagline {
    font-family: "Arimo", Arial, sans-serif;
    font-weight: 700;
    font-size: 16px;
    fill: var(--paper);
  }
  .back__brand {
    position: absolute;
    left: 40px; top: 92px;
    font-family: "Roboto Condensed", "Arial Narrow", sans-serif;
    font-weight: 700;
    font-size: 46px;
    line-height: 0.92;
    letter-spacing: 1.5px;
    color: var(--wine);
  }
  .back__divider {
    position: absolute;
    left: 250px; top: 44px;
    width: 1px; height: 120px;
    background: var(--wine);
  }
  .contact {
    position: absolute;
    left: 268px; top: 38px;
    color: var(--muted);
    font-size: 11.5px;
    line-height: 1.35;
  }
  .contact__name {
    color: var(--wine);
    font-weight: 700;
    font-size: 19px;
    letter-spacing: 0.5px;
    line-height: 1.1;
  }
  .contact__title { font-size: 12px; margin-bottom: 10px; }
  .contact__address { margin-bottom: 8px; }
  .contact__row { display: flex; align-items: center; gap: 6px; }
  .contact__row svg { width: 10px; height: 10px; fill: var(--wine); flex: none; }
</style>
</head>
<body>

  <section class="card card--front" aria-label="Card front">
    <div class="front__brand">BLUE<br>FORGE</div>
    <div class="front__cta">VISIT NOW</div>
    <div class="front__url">www.tavmontgroup.example/blue-forge</div>
  </section>

  <section class="card card--back" aria-label="Card back">
    <svg class="back__swoosh" viewBox="0 0 560 320" width="560" height="320" aria-hidden="true">
      <defs>
        <path id="tagline-curve" d="M190,308 C240,272 320,252 420,238"/>
      </defs>
      <path d="M290,236 C400,214 500,196 560,130 L560,150 C505,200 410,220 290,236 Z" fill="var(--ink)"/>
      <path d="M150,320 C200,258 300,232 400,218 C470,208 530,192 560,160 L560,320 Z" fill="var(--wine)"/>
      <text class="back__tagline"><textPath href="#tagline-curve">A Tavmont Company</textPath></text>
    </svg>

    <div class="back__brand">BLUE<br>FORGE</div>
    <div class="back__divider"></div>

    <div class="contact">
      <div class="contact__name">DANIEL HARROW</div>
      <div class="contact__title">CEO/Founder</div>
      <div class="contact__address">48 Calder Avenue, Suite 1200,<br>Lakeview, Ohio 44012</div>
      <div class="contact__row">
        <svg viewBox="0 0 10 10"><path d="M2 0.5 L3.8 2.6 L2.8 3.8 C3.5 5.3 4.7 6.5 6.2 7.2 L7.4 6.2 L9.5 8 L8.3 9.5 C4.3 9.2 0.8 5.7 0.5 1.7 Z"/></svg>
        <span>01987654320</span>
      </div>
      <div class="contact__row">
        <svg viewBox="0 0 10 10"><path d="M0.5 2 H9.5 V8.5 H0.5 Z M1.2 2.6 L5 5.6 L8.8 2.6" stroke="#ffffff" stroke-width="0.7"/></svg>
        <span>info@tavmontgroup.example</span>
      </div>
    </div>
  </section>

</body>
</html>
```